CCTV Website

We are looking for a Wordpress designer to create an e-commerce website for us. We have all the products that will be uploaded to site on csv format, so our main focus is layout, style, home page slider image selections and related site page images selection by the designer.

When project is reaching completion we will provide product files.

Industry/Entity Type

E-Commerce

```html
<!DOCTYPE html>
<html lang="en">
<head>
<meta charset="utf-8">
<title>Sentrix CCTV – Safety &amp; Security</title>
<link rel="stylesheet" href="https://fonts.googleapis.com/css2?family=Poppins:wght@400;500;600&family=Open+Sans:wght@400;600&family=Montserrat:wght@400;500;600&display=swap">
<style>
:root{
  --blue:#1e88e5;
  --blue-bright:#2196f3;
  --ink:#222;
  --text:#555;
  --muted:#888;
  --line:#e4e4e4;
  --dark-btn:#3b3b3b;
  --footer-bg:#f4f4f4;
  --star:#f5c518;
  --sale:#e53c1a;
}
*{box-sizing:border-box;margin:0;padding:0}
html,body{width:1200px;height:3689px;overflow:hidden}
body{position:relative;background:#fff;font-family:"Open Sans",sans-serif;color:var(--text)}
.abs{position:absolute}
.brand{font-family:"Poppins",sans-serif;font-weight:500;font-size:32px;color:var(--ink);display:flex;align-items:center;gap:10px}
.brand .dot{width:14px;height:14px;background:var(--blue)}
/* header */
.site-header{top:0;left:0;width:1200px;height:103px}
.site-header .brand{position:absolute;left:86px;top:30px}
.main-nav{position:absolute;right:86px;top:36px;display:flex;gap:8px;font-family:"Montserrat",sans-serif;font-size:15px;font-weight:500;color:var(--ink)}
.main-nav a{padding:6px 14px;text-decoration:none;color:inherit}
.main-nav a.active{background:var(--blue-bright);color:#fff}
/* hero */
.hero{top:103px;left:0;width:1200px;height:389px;background:linear-gradient(180deg,#5a5c60 0%,#3e4044 55%,#2c2d30 100%)}
.hero h1{position:absolute;top:160px;width:100%;text-align:center;font-family:"Poppins",sans-serif;font-weight:500;font-size:50px;color:#fff}
.hero p{position:absolute;top:222px;width:100%;text-align:center;font-family:"Poppins",sans-serif;font-size:30px;color:#fff}
.features{top:492px;left:0;width:1200px;height:108px;background:var(--blue-bright);display:flex;justify-content:center;gap:64px}
.feature{width:70px;text-align:center;color:#fff;font-family:"Poppins",sans-serif;font-weight:600;font-size:15px;padding-top:6px}
.feature svg{display:block;margin:0 auto 6px}
/* about */
.monitor{left:167px;top:713px;width:305px;height:362px;background:linear-gradient(160deg,#4a4d52 0%,#7b7f86 55%,#e2e3e5 100%)}
.about{left:585px;top:718px;width:500px}
.eyebrow{font-family:"Poppins",sans-serif;font-size:15px;color:var(--blue-bright)}
.about h2{font-family:"Poppins",sans-serif;font-weight:600;font-size:30px;color:var(--ink);margin:4px 0 14px}
.about p{font-size:13px;line-height:20px;color:var(--muted)}
.about ol{list-style:none;margin:22px 0 24px;font-size:13px;line-height:24px;color:var(--muted)}
.btn-pill{display:inline-block;background:var(--blue-bright);color:#fff;font-family:"Montserrat",sans-serif;font-weight:600;font-size:12px;border-radius:22px;text-align:center}
.about .btn-pill{width:138px;height:40px;line-height:40px}
/* section headings */
.divider{left:550px;width:100px;height:24px}
.sec-sub{left:0;width:1200px;text-align:center;font-family:"Poppins",sans-serif;font-size:16px;color:var(--ink)}
.sec-title{left:0;width:1200px;text-align:center;font-family:"Poppins",sans-serif;font-size:32px;color:var(--blue-bright)}
.filters{top:1349px;left:0;width:1200px;display:flex;justify-content:center;gap:12px}
.filters span{height:34px;line-height:32px;padding:0 22px;border:1px solid var(--line);border-radius:3px;font-family:"Montserrat",sans-serif;font-size:11px;font-weight:600;color:var(--ink)}
.filters span.on{background:var(--blue-bright);border-color:var(--blue-bright);color:#fff}
.gallery{top:1431px;left:0;width:1200px;height:541px;display:grid;grid-template-columns:repeat(3,1fr);grid-template-rows:repeat(2,1fr)}
.gallery div:nth-child(1){background:linear-gradient(135deg,#c9d6e6,#7b8aa0)}
.gallery div:nth-child(2){background:linear-gradient(135deg,#2d8cf0,#1f78d8)}
.gallery div:nth-child(3){background:linear-gradient(135deg,#9fb4c8,#dfe8ee)}
.gallery div:nth-child(4){background:linear-gradient(135deg,#e6e8ec,#8d98a8)}
.gallery div:nth-child(5){background:linear-gradient(180deg,#f2c78f,#6b6e74)}
.gallery div:nth-child(6){background:linear-gradient(135deg,#4a3a30,#b5624a)}
/* products */
.recommend{top:2050px;left:0;width:1200px;text-align:center;font-family:"Poppins",sans-serif;font-size:16px;color:var(--blue)}
.featured-title{top:2072px;left:0;width:1200px;text-align:center;font-family:"Poppins",sans-serif;font-weight:500;font-size:36px;color:var(--ink);letter-spacing:1px}
.product{top:2181px;width:231px;height:438px;border:1px solid var(--line);text-align:center}
.product .thumb{position:absolute;left:40px;top:32px;width:150px;height:185px;background:radial-gradient(circle,#d9d9d9,#f6f6f6 70%)}
.sale{position:absolute;left:90px;top:-1px;background:var(--sale);color:#fff;font-size:12px;font-weight:600;padding:2px 7px}
.price{position:absolute;top:222px;width:100%;font-family:"Open Sans",sans-serif;font-size:34px;color:var(--ink)}
.price s{font-size:14px;color:var(--muted);margin-right:6px}
.pname{position:absolute;top:272px;left:15px;right:15px;font-size:14px;line-height:19px;color:var(--ink)}
.stars{position:absolute;top:312px;width:100%;color:var(--star);font-size:11px;letter-spacing:1px}
.cart{position:absolute;left:18px;top:338px;width:195px;height:45px;line-height:45px;background:var(--dark-btn);color:#fff;font-size:14px;font-weight:600}
.actions{position:absolute;top:396px;left:18px;right:18px;display:flex;justify-content:space-between;font-size:11px;color:var(--ink)}
.view-details{left:494px;top:2661px;width:222px;height:42px;line-height:42px;font-family:"Poppins",sans-serif;font-weight:500;font-size:14px}
.secure-text{top:2900px;left:270px;width:660px;text-align:center;font-size:12px;line-height:19px;color:var(--text)}
/* promo */
.promo-img{top:3052px;width:231px;height:162px;background:linear-gradient(135deg,#f1f1f1,#dcdcdc)}
.promo{top:3052px;width:200px}
.promo h3{font-family:"Poppins",sans-serif;font-weight:400;font-size:15px;color:var(--ink);margin-bottom:16px}
.promo p{font-size:12px;line-height:18px;color:var(--text)}
.promo .outline{display:inline-block;margin-top:18px;width:146px;height:44px;line-height:38px;border:3px solid #a9cdf2;text-align:center;font-family:"Poppins",sans-serif;font-size:12px;color:var(--blue);font-weight:500}
/* footer */
.site-footer{top:3300px;left:0;width:1200px;height:389px;background:var(--footer-bg)}
.site-footer .brand{position:absolute;left:86px;top:42px}
.f-about{position:absolute;left:86px;top:106px;width:200px;font-size:11.5px;line-height:18px;color:var(--text)}
.f-about p+p{margin-top:8px}
.f-head{position:absolute;top:40px;font-family:"Poppins",sans-serif;font-weight:600;font-size:16px;color:var(--ink)}
.f-links{position:absolute;left:347px;top:82px;width:240px;list-style:none;font-size:12px;color:var(--text)}
.f-links li{height:38px;line-height:38px;border-bottom:1px solid var(--line);display:flex;align-items:center;gap:10px}
.f-links li::before{content:"";width:9px;height:9px;background:#777;border-radius:2px}
.portfolio{position:absolute;left:610px;top:82px;display:grid;grid-template-columns:repeat(3,76px);gap:6px}
.portfolio div{height:76px;background:linear-gradient(135deg,#b6c3d0,#6e7884)}
.portfolio div:nth-child(even){background:linear-gradient(135deg,#d8cfc4,#8a8077)}
.contact{position:absolute;left:873px;top:80px;width:240px;list-style:none;font-size:12px;color:var(--text)}
.contact li{display:flex;gap:12px;margin-bottom:10px;line-height:18px}
.contact svg{flex:none;margin-top:3px}
.f-bottom{position:absolute;left:86px;right:86px;top:315px;border-top:1px solid var(--line);padding-top:36px;display:flex;justify-content:space-between;font-size:11px;color:var(--muted)}
.social{display:flex;gap:22px}
.social i{width:9px;height:9px;border-radius:50%;background:#777;display:block;margin-top:3px}
</style>
</head>
<body>

<header class="abs site-header">
  <div class="brand"><span class="dot"></span>Sentrix CCTV</div>
  <nav class="main-nav">
    <a class="active">Home</a><a>About Us</a><a>Services</a><a>Technology</a><a>Security</a><a>Contact Us</a>
  </nav>
</header>

<section class="abs hero" role="img" aria-label="Three wall-mounted security cameras against a grey concrete wall">
  <h1>Safety &amp; Security</h1>
  <p>AT Your FingerTips</p>
</section>

<section class="abs features">
  <div class="feature">
    <svg width="56" height="56" viewBox="0 0 56 56" fill="none" stroke="#fff" stroke-width="2.5"><circle cx="28" cy="28" r="25"/><path d="M28 14l11 4v9c0 8-5 13-11 15-6-2-11-7-11-15v-9z"/><path d="M28 14v28M17 27h22"/></svg>
    Protection
  </div>
  <div class="feature">
    <svg width="56" height="56" viewBox="0 0 56 56" fill="none" stroke="#fff" stroke-width="2.5"><circle cx="28" cy="28" r="25"/><path d="M28 14l11 4v9c0 8-5 13-11 15-6-2-11-7-11-15v-9z"/><path d="M22 28l5 5 8-9"/></svg>
    Security
  </div>
  <div class="feature">
    <svg width="56" height="56" viewBox="0 0 56 56" fill="none" stroke="#fff" stroke-width="2.5"><circle cx="28" cy="28" r="25"/><path d="M19 30c0-6 4-10 9-10s9 4 9 10M23 36c0-2 0-4 0-6 0-3 2-5 5-5s5 2 5 5v4M28 29v10"/></svg>
    Fingerprint
  </div>
</section>

<div class="abs monitor" role="img" aria-label="Desktop monitor showing a grid of CCTV camera feeds"></div>

<div class="abs about">
  <div class="eyebrow">who we are</div>
  <h2>CCTV Show in Desktop</h2>
  <p>There are many variations of passages of Lorem Ipsum available, but the majority have suffered alteration in some form, by injected humour, or randomised words which don't look even slightly believable.</p>
  <ol>
    <li>01. Vestibulum non mauris non magna dapibus</li>
    <li>02. Suspendisse vel tellus eu elit convallis pretium eu</li>
    <li>03. Sed vitae mi efficitur, iaculis magna vitae.</li>
    <li>04. Aliquam ut quam quis nisl lacinia venenatis et et tellus.</li>
    <li>05. Proin semper magna in justo varius</li>
  </ol>
  <span class="btn-pill">CONTACT US</span>
</div>

<svg class="abs divider" style="top:1193px" viewBox="0 0 100 24"><path d="M0 12h34M66 12h34" stroke="#999" stroke-width="1"/><rect x="40" y="6" width="18" height="9" rx="1" fill="#333" transform="rotate(-12 49 10)"/><path d="M48 14l-2 7h8" stroke="#333" stroke-width="2" fill="none"/></svg>
<div class="abs sec-sub" style="top:1235px">360 °Total Security Services</div>
<div class="abs sec-title" style="top:1262px">CCTV Surveillance Systems</div>

<div class="abs filters">
  <span class="on">ALL</span><span>ALARM &amp; LOCK</span><span>CLOSED CIRCUIT</span><span>DAY &amp; NIGHT CAMS</span><span>EQUIPMENTS</span><span>WIRELESS CAMS</span>
</div>

<div class="abs gallery">
  <div role="img" aria-label="Technician fitting a security camera to a wall"></div>
  <div role="img" aria-label="Ceiling-mounted camera highlighted in blue overlay"></div>
  <div role="img" aria-label="Dome camera inside a bright office lobby"></div>
  <div role="img" aria-label="Installer mounting a camera on a ceiling"></div>
  <div role="img" aria-label="Street camera overlooking city traffic at sunset"></div>
  <div role="img" aria-label="Hands wiring a recorder unit"></div>
</div>

<div class="abs recommend">We Recommend</div>
<div class="abs featured-title">Featured Products</div>

<div class="abs product" style="left:96px">
  <div class="thumb" role="img" aria-label="Round white smoke detector"></div>
  <div class="price">$95.00</div>
  <div class="pname">Non-woven Document Bag</div>
  <div class="stars">★★★★★</div>
  <div class="cart">ADD TO CART</div>
  <div class="actions"><span>COMPARE</span><span>ADD TO WISHLIST</span></div>
</div>
<div class="abs product" style="left:354px">
  <span class="sale">SALE!</span>
  <div class="thumb" role="img" aria-label="Dual-head security floodlight camera"></div>
  <div class="price"><s>$79.00</s>$70.00</div>
  <div class="pname">Aztec Spooner 10 oz Mug</div>
  <div class="stars">★★★★★</div>
  <div class="cart">ADD TO CART</div>
  <div class="actions"><span>COMPARE</span><span>ADD TO WISHLIST</span></div>
</div>
<div class="abs product" style="left:612px">
  <div class="thumb" role="img" aria-label="White bullet security camera on stand"></div>
  <div class="price">$100.00</div>
  <div class="pname">Luxury Slim Stand Smart Case Leather Back...</div>
  <div class="stars">★★★★★</div>
  <div class="cart">ADD TO CART</div>
  <div class="actions"><span>COMPARE</span><span>ADD TO WISHLIST</span></div>
</div>
<div class="abs product" style="left:868px">
  <div class="thumb" role="img" aria-label="Four-camera kit with recorder"></div>
  <div class="price">$120.00</div>
  <div class="pname">T-Shirt Printing</div>
  <div class="stars">★★★★☆</div>
  <div class="cart">ADD TO CART</div>
  <div class="actions"><span>COMPARE</span><span>ADD TO WISHLIST</span></div>
</div>

<div class="abs btn-pill view-details">View Details</div>

<svg class="abs divider" style="top:2769px" viewBox="0 0 100 24"><path d="M0 12h34M66 12h34" stroke="#999" stroke-width="1"/><rect x="40" y="6" width="18" height="9" rx="1" fill="#333" transform="rotate(-12 49 10)"/><path d="M48 14l-2 7h8" stroke="#333" stroke-width="2" fill="none"/></svg>
<div class="abs sec-sub" style="top:2811px">360 ° Total Security Services</div>
<div class="abs sec-title" style="top:2840px">CCTV Secure <span style="font-size:22px;vertical-align:4px">360º</span> Surveillance Systems</div>
<p class="abs secure-text">Ante tincidunt tempus. Donec vitae sapien ut libero venenatis faucibus. Nullam quis ante. Etiam sit amet orci eget eros faucibus tincidunt. Sed fringilla mauris sit amet nibh. Donec sodales sagittis magna. Sed consequat, leo eget bibendum sodales, augue velit cursus nunc.</p>

<div class="abs promo-img" style="left:103px" role="img" aria-label="White bullet camera on wall bracket"></div>
<div class="abs promo" style="left:361px">
  <h3>Dom Cam</h3>
  <p>Etiam ultricies nisi vel augue. Curabitur ullamcorper ultricies nisi. Nam eget dui. Etiam rhoncus.</p>
  <span class="outline">View Products</span>
</div>
<div class="abs promo-img" style="left:617px" role="img" aria-label="White alarm keypad panel"></div>
<div class="abs promo" style="left:875px">
  <h3>Dom Cam</h3>
  <p>Etiam ultricies nisi vel augue. Curabitur ullamcorper ultricies nisi. Nam eget dui. Etiam rhoncus.</p>
  <span class="outline">View Products</span>
</div>

<footer class="abs site-footer">
  <div class="brand"><span class="dot"></span>Sentrix CCTV</div>
  <div class="f-about">
    <p>Security and privacy are two sides of the same coin. You can't have privacy without security and vice versa.</p>
    <p>Security as a topic has continued to rise in popularity in the recent couple of years, and it comes as a no surprise.</p>
  </div>
  <div class="f-head" style="left:347px">Important Links</div>
  <ul class="f-links"><li>Support</li><li>Privacy &amp; Policy</li><li>Terms &amp; Conditions</li><li>Packages</li><li>Our Network</li></ul>
  <div class="f-head" style="left:610px">Recent Portfolio</div>
  <div class="portfolio">
    <div role="img" aria-label="Camera installation"></div><div role="img" aria-label="Monitoring room"></div><div role="img" aria-label="Outdoor camera"></div>
    <div role="img" aria-label="Office camera"></div><div role="img" aria-label="Installer at work"></div><div role="img" aria-label="Recorder wiring"></div>
  </div>
  <div class="f-head" style="left:873px">Contact with us</div>
  <ul class="contact">
    <li><svg width="12" height="12" viewBox="0 0 12 12"><path d="M6 1L1 5.5h1.5V11h3V8h1v3h3V5.5H11z" fill="#333"/></svg>48 Harlow Street, Brookfield, MD 20900</li>
    <li><svg width="12" height="12" viewBox="0 0 12 12"><path d="M2 1h3l1 3-1.5 1a7 7 0 003 3L8.5 7l3 1v3c-6 0-10.5-4.5-10.5-10z" fill="#333"/></svg>+1 555-0142-386</li>
    <li><svg width="12" height="12" viewBox="0 0 12 12"><rect x="0.5" y="2" width="11" height="8" fill="#333"/><path d="M1 2.5l5 4 5-4" stroke="#fff" fill="none"/></svg>hello@sentrixcctv.com</li>
  </ul>
  <div class="f-bottom">
    <span>Copyright © 2017. All rights reserved</span>
    <div class="social"><i></i><i></i><i></i><i></i><i></i></div>
  </div>
</footer>

</body>
</html>
```